High-End audio shop owner needs a business card

I need a personal Business Card for my Audio shop which exists since 1962. We offer high Quality brands, professional Attention and run our own repair-service-department. I look for a design which will be printed on high Quality paper and shall convey trust to the Client that we are very serious. Language is german.

```html
<!DOCTYPE html>
<html lang="de">
<head>
<meta charset="utf-8">
<title>Tonhaus Lindhoff – Visitenkarte</title>
<link href="https://fonts.googleapis.com/css2?family=Open+Sans:wght@400;600&display=swap" rel="stylesheet">
<style>
  :root {
    --stage: #2b2e33;
    --paper: #ffffff;
    --ink: #6b6b6b;
    --ink-dark: #555555;
    --accent: #f26a1b;
    --night: #050505;
    --night-text: #e8e8e8;
  }
  * { box-sizing: border-box; margin: 0; padding: 0; }
  html, body { width: 1200px; height: 900px; overflow: hidden; }
  body {
    background: var(--stage);
    font-family: "Open Sans", Arial, sans-serif;
    position: relative;
  }
  .card {
    position: absolute;
    top: 300px;
    width: 525px;
    height: 300px;
    border-radius: 20px;
    overflow: hidden;
    box-shadow: 0 14px 30px rgba(0,0,0,.35);
  }
  .card--front { left: 45px; background: var(--paper); }
  .card--back { left: 630px; background: var(--night); }

  .front__band {
    position: absolute; left: 0; right: 0; bottom: 0;
    height: 38px; background: var(--accent);
  }
  .person { position: absolute; left: 34px; top: 30px; }
  .person__name {
    font-size: 27px; font-weight: 400; color: var(--ink);
    letter-spacing: -0.5px; line-height: 1;
  }
  .person__role {
    font-size: 11px; font-weight: 600; color: var(--accent);
    margin-top: 6px; letter-spacing: .5px;
  }
  .front__rule {
    position: absolute; left: 112px; right: 26px; top: 82px;
    height: 2px; background: var(--accent);
  }
  .contact { position: absolute; left: 34px; top: 100px; list-style: none; }
  .contact li {
    display: flex; align-items: center; gap: 9px;
    font-size: 13px; color: var(--ink-dark); margin-bottom: 8px;
  }
  .contact svg { width: 11px; height: 11px; flex: none; }
  .brand {
    position: absolute;
    font-weight: 400;
    display: flex; align-items: center; gap: 10px;
    white-space: nowrap;
    letter-spacing: .5px;
  }
  .brand__mark { width: 10px; height: 10px; }
  .card--front .brand { right: 34px; top: 130px; font-size: 24px; color: var(--ink-dark); }
  .card--front .brand__mark { background: var(--ink-dark); }
  .address {
    position: absolute; right: 34px; bottom: 56px;
    text-align: right; font-size: 14px; line-height: 1.55; color: var(--ink);
  }
  .card--back .brand {
    left: 50%; top: 50%; transform: translate(-50%, -50%);
    font-size: 38px; gap: 14px; color: var(--night-text);
  }
  .card--back .brand__mark { width: 14px; height: 14px; background: var(--night-text); }
</style>
</head>
<body>
  <section class="card card--front" aria-label="Vorderseite">
    <div class="person">
      <p class="person__name">YOUR NAME</p>
      <p class="person__role">OWNER</p>
    </div>
    <div class="front__rule"></div>
    <ul class="contact">
      <li>
        <svg viewBox="0 0 12 12"><path d="M3 1 L5 3.5 L4 5 Q5 7 7 8 L8.5 7 L11 9 L10 11 Q4 11 1 4 Z" fill="#f26a1b"/></svg>
        000 000 0000
      </li>
      <li>
        <svg viewBox="0 0 12 12"><rect x="1" y="2.5" width="10" height="7" rx="1" fill="#f26a1b"/><path d="M1.5 3 L6 6.5 L10.5 3" stroke="#fff" stroke-width="1" fill="none"/></svg>
        youremail@xyz.com
      </li>
      <li>
        <svg viewBox="0 0 12 12"><circle cx="6" cy="6" r="5" fill="#f26a1b"/><path d="M1 6 H11 M6 1 Q3 6 6 11 M6 1 Q9 6 6 11" stroke="#fff" stroke-width=".8" fill="none"/></svg>
        www.yourwebsite.com
      </li>
    </ul>
    <div class="brand"><span class="brand__mark"></span>Tonhaus Lindhoff</div>
    <p class="address">0000, Street Name<br>City, State 0000</p>
    <div class="front__band"></div>
  </section>

  <section class="card card--back" aria-label="Rückseite">
    <div class="brand"><span class="brand__mark"></span>Tonhaus Lindhoff</div>
  </section>
</body>
</html>
```